Copperleaf Motorized Shade Business Card

Hello, we've had our logo made. Now we are looking for a clean and cool looking business card. One side can just be the logo with any design elements that might look good with it. The other side will be Name, Phone Number and Email. There will not be an address on the card.

```html
<!DOCTYPE html>
<html lang="en">
<head>
<meta charset="utf-8">
<title>Copperleaf Motorized Shade – Business Card</title>
<link href="https://fonts.googleapis.com/css2?family=Montserrat:wght@400;500;600;700&family=Signika:wght@400&display=swap" rel="stylesheet">
<style>
  :root {
    --stage: #222831;
    --label: #a9adb3;
    --navy: #173f79;
    --navy-deep: #0f3a73;
    --sky: #08aee9;
    --sun: #ffc20e;
    --paper: #ffffff;
  }
  * { margin: 0; padding: 0; box-sizing: border-box; }
  html, body {
    width: 1200px; height: 663px; overflow: hidden;
    background: var(--stage);
  }
  .stage { position: relative; width: 1200px; height: 663px; }

  .view-label {
    position: absolute; top: 126px;
    font-family: "Signika", sans-serif; font-size: 23px;
    color: var(--label);
  }
  .view-label--front { left: 113px; }
  .view-label--back { left: 619px; }

  .card {
    position: absolute; top: 176px;
    width: 467px; height: 311px; overflow: hidden;
    font-family: "Montserrat", sans-serif;
  }
  .card--front { left: 113px; background: var(--paper); }
  .card--back {
    left: 621px;
    background: linear-gradient(165deg, #1b3e78 0%, #124a84 40%, #06609a 65%, var(--sky) 100%);
  }
  .card svg { position: absolute; inset: 0; }

  .brand-name {
    position: absolute; left: 0; right: 0; top: 112px;
    text-align: center;
    font-weight: 700; font-size: 27px; line-height: 1.2;
    color: var(--navy-deep);
  }

  .holder-name {
    position: absolute; right: 43px; top: 42px;
    font-weight: 700; font-size: 31px; letter-spacing: -0.5px;
    color: var(--sun); line-height: 1;
  }
  .holder-role {
    position: absolute; right: 43px; top: 82px;
    font-weight: 600; font-size: 10px; letter-spacing: 4px;
    color: var(--paper); margin-right: -4px;
  }
  .contact { position: absolute; left: 48px; top: 212px; }
  .contact-phone {
    font-weight: 700; font-size: 29px; color: var(--navy-deep);
    line-height: 1; margin-bottom: 9px;
  }
  .contact-email { font-size: 14px; color: var(--sky); line-height: 18px; }
  .contact-web { font-size: 14px; color: var(--navy-deep); line-height: 18px; }
</style>
</head>
<body>
<main class="stage">
  <h2 class="view-label view-label--front">Front View</h2>
  <h2 class="view-label view-label--back">Back View</h2>

  <section class="card card--front" aria-label="Card front">
    <svg viewBox="0 0 467 311" width="467" height="311" aria-hidden="true">
      <defs>
        <linearGradient id="front-band" x1="0" y1="0" x2="1" y2="0">
          <stop offset="0" stop-color="#066ea6"/>
          <stop offset="0.35" stop-color="#04558a"/>
          <stop offset="0.75" stop-color="#173f79"/>
          <stop offset="1" stop-color="#173f79"/>
        </linearGradient>
      </defs>
      <path d="M0,290 Q233,258 467,290 L467,311 L0,311 Z" fill="var(--sun)"/>
      <path d="M0,297 Q233,263 467,297 L467,311 L0,311 Z" fill="url(#front-band)"/>
    </svg>
    <p class="brand-name">Copperleaf<br>Motorized Shade</p>
  </section>

  <section class="card card--back" aria-label="Card back">
    <svg viewBox="0 0 467 311" width="467" height="311" aria-hidden="true">
      <path d="M0,197 C50,178 100,168 150,168 C255,170 335,240 384,311 L0,311 Z" fill="var(--sun)"/>
      <path d="M0,200 C50,181 100,172 150,172 C250,175 322,242 368,311 L0,311 Z" fill="var(--paper)"/>
    </svg>
    <h1 class="holder-name">YOUR NAME</h1>
    <p class="holder-role">FOUNDER/CEO</p>
    <div class="contact">
      <p class="contact-phone">123.456.7890</p>
      <p class="contact-email">hello@copperleafshade.com</p>
      <p class="contact-web">www.copperleafshade.com</p>
    </div>
  </section>
</main>
</body>
</html>
```